Gourmet cookie company needs a label designed

We need a label designed for a new cookie company. We make mini cookies. The labels will be placed on either white tins or clear containers. We would like some bright and eye catching label although not child like. Our target customer is adults not kids.
Any color/colors acceptable. The initial label will be a square 4" label but the design should also be able to be formatted to fit on a round label as well in the future.

Text on label: Rosalind's Wafer Crumb Company; Chocolate Chip; All Natural; New Wt. 8.0oz

```html
<!DOCTYPE html>
<html lang="en">
<head>
<meta charset="utf-8">
<title>Rosalind's Wafer Crumb Co. – Chocolate Chip Label</title>
<link href="https://fonts.googleapis.com/css2?family=Delius&family=Questrial&display=swap" rel="stylesheet">
<style>
  :root {
    --cocoa: #55290a;
    --bark: #4a1806;
    --caramel: #5e3612;
    --paper: #ffffff;
  }
  html, body {
    margin: 0;
    padding: 0;
    width: 1200px;
    height: 1130px;
    overflow: hidden;
    background: var(--paper);
  }
  .label {
    position: relative;
    width: 1200px;
    height: 1130px;
    background: var(--paper);
  }
  .brand-name {
    position: absolute;
    left: 0;
    top: 170px;
    width: 1200px;
    margin: 0;
    text-align: center;
    font-family: "Delius", cursive;
    font-weight: 400;
    font-size: 112px;
    line-height: 1.15;
    color: var(--cocoa);
  }
  .claim {
    position: absolute;
    left: 0;
    top: 776px;
    width: 1260px;
    margin: 0;
    text-align: center;
    font-family: "Questrial", sans-serif;
    font-size: 50px;
    letter-spacing: -1px;
    line-height: 1;
    color: var(--caramel);
  }
  .flavour-band {
    position: absolute;
    left: 73px;
    top: 864px;
    width: 1127px;
    height: 205px;
    background: var(--bark);
    display: flex;
    align-items: center;
    justify-content: center;
  }
  .flavour {
    margin: 0;
    font-family: "Delius", cursive;
    font-weight: 400;
    font-size: 128px;
    line-height: 1;
    color: var(--paper);
    letter-spacing: 2px;
  }
  .net-weight {
    position: absolute;
    left: 0;
    top: 1090px;
    width: 1260px;
    margin: 0;
    text-align: center;
    font-family: "Questrial", sans-serif;
    font-size: 31px;
    letter-spacing: -0.5px;
    line-height: 1;
    color: var(--caramel);
  }
</style>
</head>
<body>
  <main class="label">
    <h1 class="brand-name">Rosalind's<br>Wafer Crumb Co.</h1>
    <p class="claim">ALL NATURAL</p>
    <div class="flavour-band">
      <p class="flavour">chocolate chip</p>
    </div>
    <p class="net-weight">NET WT. 8.0oz</p>
  </main>
</body>
</html>
```